Social responsible Renewable Energy company

We at voltaQ are an independent power producer company founded in 2021 that handles large scale deployment of Renewable Energy and carbon neutral Energy as a service model. We offer turnkey solutions using solar panel systems and this could be incorporated in our business cards. You can also find our logo in the documents provided. Another key issue is that the business cards will be printed on recicled paper, not sure if this is a limitation in deciding the design. The recycled sign should also be added on the business card and stating that the paper used was recycled. Our website is www.myvoltaq.example. It should also be very professional, not too dreamy but still needs to capture your imagination. We are really excited to get your ideas !

Target Market(s)

Renewable Energy market

Contact Information for Business Card

The business card will be printed on recycled paper. Name of the company is voltaQ. Website is www.myvoltaq.example

Requirements
Nice to have
• Our motto: Powered by renewable, driven by people.

```html
<!DOCTYPE html>
<html lang="en">
<head>
<meta charset="utf-8">
<title>voltaQ business card</title>
<link href="https://fonts.googleapis.com/css2?family=Poppins:wght@400;500;600;700&display=swap" rel="stylesheet">
<style>
  :root {
    --stage: #1c1e21;
    --paper: #ffffff;
    --navy: #1e4a7c;
    --blue: #2f7cc4;
    --ink: #1f4f86;
    --back: #1f4f82;
    --back-pattern: #23588f;
    --badge: #3b5d3a;
  }
  * { box-sizing: border-box; margin: 0; padding: 0; }
  html, body { width: 1200px; height: 900px; overflow: hidden; }
  body {
    background: var(--stage);
    font-family: "Poppins", sans-serif;
    display: flex; flex-direction: column; align-items: center; justify-content: center;
    gap: 50px;
  }
  .card { width: 630px; height: 360px; position: relative; overflow: hidden; box-shadow: 0 10px 30px rgba(0,0,0,.5); }
  .card-front { background: var(--paper); }
  .holder { position: absolute; left: 40px; top: 36px; }
  .holder-name { font-size: 28px; font-weight: 600; color: var(--navy); letter-spacing: 1px; line-height: 1.1; }
  .holder-role { font-size: 17px; font-weight: 400; color: var(--blue); letter-spacing: 1px; }
  .contact { position: absolute; left: 40px; top: 140px; color: var(--ink); font-size: 15px; line-height: 1.55; }
  .address { margin-bottom: 8px; }
  .contact-line { display: flex; align-items: center; gap: 8px; }
  .contact-line svg { width: 14px; height: 14px; fill: var(--blue); flex: none; }
  .brand-name { position: absolute; right: 46px; top: 128px; font-size: 82px; font-weight: 600; color: var(--navy); letter-spacing: 2px; }
  .recycled-badge { position: absolute; left: 400px; top: 286px; width: 118px; height: 44px; border-radius: 3px; background: var(--badge); }
  .card-back { background: var(--back); }
  .back-pattern { position: absolute; inset: 0; background: linear-gradient(135deg, var(--back-pattern), var(--back) 60%, var(--back-pattern)); }
  .back-brand { position: absolute; right: 50px; bottom: 40px; font-size: 46px; font-weight: 600; color: #fff; letter-spacing: 2px; }
</style>
</head>
<body>
  <section class="card card-front">
    <div class="holder">
      <p class="holder-name">Daniel Moreau</p>
      <p class="holder-role">CEO/Founder</p>
    </div>
    <div class="contact">
      <p class="address">418 Harbor Lane West<br>Suite 210, Lakeview<br>OR 97630</p>
      <p class="contact-line"><svg viewBox="0 0 24 24"><path d="M6.6 10.8a15.1 15.1 0 0 0 6.6 6.6l2.2-2.2a1 1 0 0 1 1-.25 11.4 11.4 0 0 0 3.6.57 1 1 0 0 1 1 1V20a1 1 0 0 1-1 1A17 17 0 0 1 3 4a1 1 0 0 1 1-1h3.5a1 1 0 0 1 1 1c0 1.25.2 2.45.57 3.57a1 1 0 0 1-.25 1z"/></svg>555-014-2786</p>
      <p class="contact-line"><svg viewBox="0 0 24 24"><path d="M2 5h20v14H2z M2 5l10 8 10-8" stroke="#fff" stroke-width="1.5"/></svg>daniel@voltaq.example</p>
      <p class="contact-line"><svg viewBox="0 0 24 24"><circle cx="12" cy="12" r="10"/><path d="M2 12h20M12 2c3 3 3 17 0 20M12 2c-3 3-3 17 0 20" stroke="#fff" stroke-width="1.3" fill="none"/></svg>www.myvoltaq.example</p>
    </div>
    <p class="brand-name">voltaQ</p>
    <div class="recycled-badge" role="img" aria-label="Recycled paper certification badge"></div>
  </section>
  <section class="card card-back">
    <div class="back-pattern" role="img" aria-label="Repeating embossed brand name pattern"></div>
    <p class="back-brand">voltaQ</p>
  </section>
</body>
</html>
```